M25 Billboard Advert Required Please

I need an advert for a motorway Billboard on the M25 , the advert should show the following in big letters:
GUTTER CLEANING
TOMSDRAINWORKS.NET and a small logo off to the side (Our logo is attached)

The printer has requested the following (Important please) the advert has to be
pdf file / 300 dpi/landscape orientation / scaled to a minimum 25% advert size ( this particular site is 22ft x 10ft so 25% of this please). Please also make sure that the artwork is embedded and outlined correctly if this is incorrect it will affect the printing of the banner.
Updates

Need extra days to review

Target Market(s)

General Public

Industry/Entity Type

Gutter Cleaning

Requirements
Should not have
• No Change to our Logo

```html
<!DOCTYPE html>
<html lang="en">
<head>
<meta charset="utf-8">
<title>Gutter Cleaning Billboard</title>
<link href="https://fonts.googleapis.com/css2?family=Montserrat:ital,wght@0,700;1,600;1,800&family=Open+Sans:wght@700&display=swap" rel="stylesheet">
<style>
  :root {
    --backdrop: #dcdcdc;
    --board: #ffffff;
    --ink: #0f0f0f;
    --brand-red: #c01824;
    --reverse: #ffffff;
  }
  html, body {
    margin: 0;
    padding: 0;
    width: 1061px;
    height: 1200px;
    overflow: hidden;
    background: var(--backdrop);
  }
  .billboard {
    position: absolute;
    left: 30px;
    top: 372px;
    width: 1000px;
    height: 455px;
    display: block;
    background: var(--board);
  }
  .headline {
    font-family: "Montserrat", sans-serif;
    font-style: italic;
    font-weight: 800;
  }
  .headline--black { fill: var(--ink); font-size: 330px; }
  .headline--red { fill: var(--brand-red); font-size: 262px; }
  .band--red { fill: var(--brand-red); }
  .band--black { fill: var(--ink); }
  .web-address {
    font-family: "Montserrat", sans-serif;
    font-style: italic;
    font-weight: 600;
    font-size: 84px;
    fill: var(--reverse);
  }
  .brand-name {
    font-family: "Montserrat", sans-serif;
    font-weight: 700;
    font-size: 30px;
    fill: var(--ink);
  }
  .brand-mark { fill: var(--brand-red); }
  .brand-tagline {
    font-family: "Open Sans", sans-serif;
    font-weight: 700;
    font-size: 15.5px;
    fill: var(--ink);
  }
</style>
</head>
<body>
  <svg class="billboard" viewBox="0 0 1627 740" xmlns="http://www.w3.org/2000/svg">
    <rect width="1627" height="740" fill="var(--board)"/>

    <text class="headline headline--black" x="154" y="283" textLength="1335" lengthAdjust="spacingAndGlyphs">GUTTER</text>
    <text class="headline headline--red" x="149" y="500" textLength="1340" lengthAdjust="spacingAndGlyphs">CLEANING</text>

    <polygon class="band--red" points="0,508 1329,508 1256,570 0,570"/>
    <polygon class="band--black" points="1329,508 1627,508 1627,568 1344,568 1147,740 1054,740 1119,683 0,683 0,570 1256,570"/>
    <polygon class="band--red" points="0,683 1119,683 1054,740 0,740"/>

    <text class="web-address" x="146" y="650" textLength="1078" lengthAdjust="spacingAndGlyphs">WWW.TOMSDRAINWORKS.NET</text>

    <g class="brand">
      <rect class="brand-mark" x="1296" y="640" width="18" height="18"/>
      <text class="brand-name" x="1589" y="661" text-anchor="end">Tom's Drainworks</text>
      <text class="brand-tagline" x="1589" y="695" text-anchor="end">Clean gutters protect your property</text>
    </g>
  </svg>
</body>
</html>
```